Civic Counsel and Advocacy Alliance Event

Situation:
- Civic Counsel and Advocacy Alliance will host a fundraising event at Cellar of Amber Oak to create fundraising momentum for the year
- Event tickets will be $200
- The event will be a social/networking event for professional in the Detroit area
- DJ Lowell Varnick, a well know Detroit area DJ will DJ the event
- Hon. Marla Penwright-Osei, M.Ed. will be the featured speaker/host of the event
- CCA CEO will also be a speaker
- Proceeds from the event will go toward expungement, which is a hot top in Michigan, as s new expungement reform law has been enacted in the state

Objectives:
- Raise fund through ticket sales to support expungement and general CCA programs/services
- Gain event sponsors

Messaging:
- Highlight details about the event and the wine tasting/networking experience
- Inspire people to attend the event in support of a worthy cause
- Event Details:
- Event Name: The Vintage & Supper Soirée
o Date: Thursday, September 30, 2021
o Time: 5:30 PM – 8:30 PM
o Space limited, get your ticket today to ensure access to this exclusive event
o Sample various high-quality wines and custom pairings, while helping Civic Counsel and Advocacy Alliance make a difference in our community.
o Proceeds from the event will support Expungement, Domestic Violence prevention, an various CCA programs helping those in need of legal representation.

Target Market(s)

- Attorneys/Professionals in Southeast Michigan - Affluent donors/philanthropist

Industry/Entity Type

Legal/Networking Event

Colors
0054AA
0677BA
7BADD7
CADEEF
E8F1F8
FFF300
FFF600
FEFA6F
FFFEC7
FFFEE8

Requirements
Nice to have
• Must be fun and inviting

```html
<!DOCTYPE html>
<html lang="en">
<head>
<meta charset="utf-8">
<title>The Vintage &amp; Supper Soirée</title>
<link rel="stylesheet" href="https://fonts.googleapis.com/css2?family=Marcellus&family=Montserrat:wght@500;600&family=Playfair+Display:wght@700&family=Alegreya:wght@700;800&display=swap">
<style>
  :root {
    --navy: #0b1a3d;
    --title-blue: #213d72;
    --ink: #2a2d3f;
    --amber-light: #f6d6a4;
    --amber: #e8b472;
    --amber-deep: #c98f4c;
    --white: #ffffff;
  }
  html, body { margin: 0; padding: 0; overflow: hidden; }
  .poster {
    position: relative;
    width: 848px;
    height: 1200px;
    overflow: hidden;
    background: var(--amber);
    font-family: "Montserrat", sans-serif;
  }
  .backdrop {
    position: absolute; inset: 0;
    background:
      radial-gradient(ellipse 260px 700px at 430px 520px, rgba(150,95,40,0.35), transparent 70%),
      radial-gradient(ellipse 180px 600px at 160px 600px, rgba(150,95,40,0.28), transparent 70%),
      radial-gradient(ellipse 170px 600px at 790px 560px, rgba(255,235,200,0.45), transparent 70%),
      linear-gradient(180deg, var(--amber-light) 0%, var(--amber) 45%, var(--amber-deep) 100%);
  }
  .org {
    position: absolute; top: 25px; left: 280px;
    display: flex; align-items: center; gap: 10px;
  }
  .org-dot {
    width: 60px; height: 60px; border-radius: 50%;
    background: var(--title-blue);
  }
  .org-name {
    font-family: "Marcellus", serif;
    color: var(--title-blue);
    font-size: 13px; line-height: 16px; letter-spacing: 0.5px;
    width: 230px;
  }
  .centered { position: absolute; left: 0; width: 848px; text-align: center; }
  .present { top: 96px; font-size: 28px; font-weight: 500; color: var(--title-blue); letter-spacing: 1px; }
  .title {
    top: 146px; margin: 0;
    font-family: "Marcellus", serif; font-weight: 400;
    font-size: 76px; line-height: 92px; color: var(--title-blue);
    letter-spacing: 1px;
  }
  .when { top: 450px; color: var(--ink); font-weight: 600; font-size: 28px; line-height: 42px; letter-spacing: 1px; }
  .speaker { top: 548px; color: var(--title-blue); font-weight: 500; font-size: 21px; line-height: 26px; letter-spacing: 1px; }
  .tickets {
    position: absolute; left: 0; top: 662px; width: 221px; height: 105px;
    background: var(--navy); color: var(--white); text-align: center;
  }
  .tickets-label { display: block; margin-top: 16px; font-size: 21px; font-weight: 500; letter-spacing: 1px; }
  .tickets-price { display: block; font-family: "Playfair Display", serif; font-weight: 700; font-size: 38px; line-height: 44px; }
  .performance {
    position: absolute; left: 540px; top: 660px; width: 260px; text-align: center;
    font-family: "Alegreya", serif; color: var(--navy);
  }
  .performance-label { display: block; font-size: 19px; font-weight: 700; }
  .performance-name { display: block; font-size: 30px; font-weight: 800; line-height: 36px; }
  .photo { position: absolute; box-shadow: 0 2px 6px rgba(0,0,0,0.3); }
  .photo-tasting {
    left: -10px; top: 810px; width: 305px; height: 235px;
    transform: rotate(-8deg);
    background: linear-gradient(135deg, #2a2624, #5b4a3e 55%, #2d2a28);
  }
  .photo-cellar {
    left: 277px; top: 839px; width: 300px; height: 202px;
    background: linear-gradient(160deg, #d9d6d1, #8f8478 50%, #3a3530);
  }
  .photo-dj {
    left: 552px; top: 758px; width: 262px; height: 262px; border-radius: 50%;
    border: 4px solid var(--white);
    background: radial-gradient(circle at 45% 40%, #f2efe9, #6b5a4a 60%, #1e1b1a);
  }
  .details {
    position: absolute; left: 0; top: 1065px; width: 848px; height: 135px;
    background: var(--navy); color: var(--white);
  }
  .details ul { margin: 0; padding: 25px 30px 0 44px; font-size: 14px; line-height: 18.5px; }
</style>
</head>
<body>
<main class="poster">
  <div class="backdrop" role="img" aria-label="Warm amber close-up of wine bottles"></div>

  <div class="org">
    <span class="org-dot"></span>
    <span class="org-name">CIVIC COUNSEL AND ADVOCACY ALLIANCE</span>
  </div>

  <div class="centered present">Present</div>
  <h1 class="centered title">THE VINTAGE &amp;<br>SUPPER<br>SOIRÉE</h1>

  <div class="centered when">Thursday, September 30, 2021<br>5:30 PM – 8:30 PM</div>

  <div class="centered speaker">Speaker:<br>Hon. Marla Penwright-Osei, M.Ed.<br>CCA CEO</div>

  <div class="tickets">
    <span class="tickets-label">Event tickets</span>
    <span class="tickets-price">$200</span>
  </div>

  <div class="performance">
    <span class="performance-label">Special Performance</span>
    <span class="performance-name">DJ Lowell Varnick</span>
  </div>

  <div class="photo photo-tasting" role="img" aria-label="Guests around a table with wine glasses and a charcuterie board"></div>
  <div class="photo photo-cellar" role="img" aria-label="Guests tasting wine in a cellar room lined with bottles"></div>
  <div class="photo photo-dj" role="img" aria-label="DJ with headphones at the mixing deck"></div>

  <section class="details">
    <ul>
      <li>Space limited, get your ticket today to ensure access to this exclusive event</li>
      <li>Sample various high-quality wines and custom pairings, while helping Civic Counsel and Advocacy Alliance make a difference in our community.</li>
      <li>Proceeds from the event will support Expungement, Domestic Violence prevention, an various CCA programs helping those in need of legal representation</li>
    </ul>
  </section>
</main>
</body>
</html>
```